Re make of the website. A fine diamond jeweller based in Melbourne Australia.

We would like the website redesigned. http://hollisfenwick.com.au/

Current website is very dated and we would like it re made and updated. An example of what we would like is https://www.taryndulcette.com/au/ or https://brindlecove.co.nz/

We sell high end diamond jewellery and the main purpose of the website will be to get people to enquire and make a booking to design a ring/meet with the experts in store. There is also a small online store.

Target Market(s)

High Affluence 25-70

Number of Pages Required

5+ page

Font styles to use
Sans Serif
Other font styles liked:
• Muli Fine

Requirements
Must have
• All the current features on the website
• Very elegant
• Main cover image
• Lots of lifestyle imagers - less blank space
• 1. Online Shop
• 2. Home page
• 3. Contact us/enquiry page
• 4. Jewellery Page
• 5. About page

```html
<!DOCTYPE html>
<html lang="en">
<head>
<meta charset="utf-8">
<title>Hollis Fenwick – Fine Diamond Jewellery</title>
<link rel="stylesheet" href="https://fonts.googleapis.com/css2?family=Tinos&family=Mulish:wght@400;600&display=swap">
<style>
:root{
  --bg:#1c1c1c;
  --bg-deep:#131313;
  --bg-mid:#232323;
  --bg-soft:#2a2a2a;
  --ink:#ffffff;
  --ink-soft:#bdbdbd;
  --ink-dim:#8a8a8a;
  --line:#5a5a5a;
  --accent:#b28b79;
  --btn:#3a3a3a;
  --field:#f2f2f2;
}
*{box-sizing:border-box;margin:0;padding:0}
html,body{width:1200px;height:4500px;overflow:hidden}
body{position:relative;background:var(--bg);color:var(--ink);font-family:"Mulish",Arial,sans-serif}
.abs{position:absolute}
.bands{position:absolute;left:0;top:0}
.serif{font-family:"Tinos","Times New Roman",serif}
.heading{font-family:"Tinos","Times New Roman",serif;font-size:29px;color:var(--ink);font-weight:400}
.center{text-align:center;left:0;width:1200px}
.copy{font-size:13px;line-height:20px;color:var(--ink-soft)}
.btn{position:absolute;display:flex;align-items:center;justify-content:center;font-size:12px;letter-spacing:.5px;color:var(--ink);border:1px solid var(--line);text-transform:uppercase}
.btn.fill{background:var(--btn);border-color:var(--btn)}
.photo{position:absolute}
/* header */
.nav{top:34px;left:40px;display:flex;gap:26px;font-size:13px;color:var(--ink-soft)}
.nav .active{color:var(--ink);border-bottom:2px solid var(--ink);padding-bottom:6px}
.brand-tab{left:512px;top:0;width:176px;height:86px;background:#fff;display:flex;flex-direction:column;align-items:center;justify-content:center;gap:6px}
.brand-tab .mark{width:26px;height:26px;background:#111}
.brand-tab .name{font-family:"Tinos",serif;font-size:18px;color:#111;letter-spacing:1px}
.search{left:748px;top:28px;width:212px;height:26px;background:#3b3b3b;font-size:11px;color:var(--ink-soft);padding:6px 10px}
.account{left:980px;top:33px;font-size:12px;color:var(--ink-soft)}
.divider{position:absolute;left:500px;width:200px;height:14px}
.tabs{top:1535px;left:420px;display:flex;gap:36px;font-size:12px;color:var(--ink-dim)}
.tabs .on{color:var(--ink);border-bottom:1px solid var(--ink);padding-bottom:4px}
.service{position:absolute;width:165px;height:44px;border:1px solid var(--line);font-size:11px;display:flex;align-items:center;justify-content:center;color:var(--ink)}
.service-icon{position:absolute;width:28px;height:28px;background:#fff;border-radius:3px}
.footer-links{font-size:12px;color:var(--ink-soft);line-height:28px}
.field{left:352px;top:4232px;width:300px;height:36px;background:var(--field);color:#555;font-size:12px;padding:10px 12px}
</style>
</head>
<body>

<svg class="bands" width="1200" height="4500" aria-hidden="true">
  <rect width="1200" height="4500" fill="#1c1c1c"/>
  <polygon points="0,560 1200,480 1200,1300 0,1240" fill="#141414"/>
  <polygon points="0,1240 1200,1300 1200,2000 0,2080" fill="#1a1a1a"/>
  <polygon points="0,2080 1200,2000 1200,2700 0,2780" fill="#252525"/>
  <polygon points="0,2780 1200,2700 1200,3360 0,3440" fill="#1a1a1a"/>
  <polygon points="0,3440 1200,3360 1200,4000 0,4110" fill="#232323"/>
  <polygon points="0,4110 1200,4000 1200,4500 0,4500" fill="#181818"/>
  <rect y="4420" width="1200" height="80" fill="#131313"/>
</svg>

<!-- Header -->
<nav class="abs nav"><span class="active">Home</span><span>Contact us</span><span>Jewellery</span><span>About Us</span><span>Online Shop</span></nav>
<div class="abs brand-tab"><span class="mark"></span><span class="name">Hollis Fenwick</span></div>
<div class="abs search">Search your Keyword</div>
<div class="abs account">Login &nbsp;|&nbsp; Register</div>
<svg class="abs" style="left:1098px;top:32px" width="60" height="18" aria-hidden="true">
  <path d="M8 15 L2 8 A3.5 3.5 0 0 1 8 4 A3.5 3.5 0 0 1 14 8 Z" fill="#fff"/>
  <rect x="38" y="6" width="14" height="10" fill="#fff"/><path d="M41 6 a4 4 0 0 1 8 0" stroke="#fff" fill="none" stroke-width="1.5"/>
</svg>

<!-- Hero -->
<div class="photo" role="img" aria-label="Emerald-cut diamond engagement ring with pavé band" style="left:160px;top:100px;width:360px;height:450px;background:radial-gradient(ellipse at 50% 45%,#e8e8e8 0%,#9a9a9a 35%,#1c1c1c 70%)"></div>
<h1 class="abs serif" style="left:606px;top:228px;font-size:48px;font-weight:400;letter-spacing:1px">ENGAGEMENT RING</h1>
<p class="abs copy" style="left:600px;top:290px;width:440px;text-align:right">For Hollis Fenwick are Australia's premier fine jewellery designers and diamond specialists, featuring an exclusive range of quality jewellery plus an expert made-to-order service.</p>
<div class="btn" style="left:745px;top:372px;width:140px;height:38px">View Collection</div>
<div class="btn fill" style="left:900px;top:372px;width:140px;height:38px">Shop Now !</div>
<svg class="abs" style="left:0;top:290px" width="1200" height="90" aria-hidden="true">
  <path d="M112 10 L80 45 L112 80" stroke="#aaa" fill="none" stroke-width="2"/>
  <path d="M1088 10 L1120 45 L1088 80" stroke="#aaa" fill="none" stroke-width="2"/>
</svg>
<svg class="abs" style="left:570px;top:560px" width="60" height="60" aria-hidden="true">
  <circle cx="30" cy="30" r="26" fill="#fff"/>
  <path d="M20 22 L30 31 L40 22 M20 30 L30 39 L40 30" stroke="#111" stroke-width="2.5" fill="none"/>
</svg>

<!-- About -->
<h2 class="abs heading" style="left:165px;top:822px">About Our Diamond</h2>
<svg class="abs" style="left:165px;top:885px" width="110" height="12" aria-hidden="true"><line x1="0" y1="6" x2="70" y2="6" stroke="#ccc"/><rect x="72" y="2" width="8" height="8" transform="rotate(45 76 6)" fill="none" stroke="#ccc"/><line x1="84" y1="6" x2="110" y2="6" stroke="#ccc"/></svg>
<p class="abs copy" style="left:165px;top:935px;width:340px;font-size:12.5px">Hollis Fenwick diamonds are carefully selected by an expert team of diamantaires to ensure consistent high quality. Our selection criteria is stricter than all our domestic and international competitors and our specialisation and volume also ensure finer value in your purchase.</p>
<div class="btn" style="left:165px;top:1085px;width:110px;height:34px;font-size:11px">Read More</div>
<div class="abs" style="left:590px;top:722px;width:450px;height:496px;border:1px solid var(--line)"></div>
<div class="photo" role="img" aria-label="Portrait of a woman wearing diamond drop earrings and rings" style="left:592px;top:738px;width:444px;height:476px;background:linear-gradient(135deg,#6b4a3a,#c49a82 45%,#8a6654 75%,#3b2a22)"></div>

<!-- Collection -->
<h2 class="abs heading center" style="top:1415px">Collection Of Diamond Ring</h2>
<svg class="divider" style="top:1482px" aria-hidden="true"><line x1="0" y1="7" x2="88" y2="7" stroke="#ccc"/><rect x="95" y="3" width="8" height="8" transform="rotate(45 99 7)" fill="none" stroke="#ccc"/><line x1="112" y1="7" x2="200" y2="7" stroke="#ccc"/></svg>
<div class="abs tabs"><span class="on">For love</span><span>For Beauty</span><span>For Men</span><span>Perma Diamond</span></div>
<svg class="abs" style="left:0;top:1580px" width="1200" height="270" aria-hidden="true">
  <g stroke="#5a5a5a" fill="none">
    <polygon points="180,135 300,15 420,135 300,255"/>
    <polygon points="420,135 540,15 660,135 540,255"/>
    <polygon points="780,135 900,15 1020,135 900,255"/>
    <line x1="0" y1="40" x2="180" y2="135"/><line x1="0" y1="230" x2="180" y2="135"/>
    <line x1="1020" y1="135" x2="1200" y2="40"/><line x1="1020" y1="135" x2="1200" y2="230"/>
    <polygon points="20,135 180,15 340,135 180,255" opacity=".5"/>
  </g>
  <polygon points="600,15 720,135 600,255 480,135" fill="#b28b79"/>
  <path d="M60 120 L45 135 L60 150" stroke="#888" fill="none" stroke-width="2"/>
  <path d="M1140 120 L1155 135 L1140 150" stroke="#888" fill="none" stroke-width="2"/>
</svg>
<div class="photo" role="img" aria-label="Solitaire diamond ring" style="left:250px;top:1665px;width:100px;height:100px;border-radius:50%;background:radial-gradient(#f4f4f4,#8c8c8c 60%,transparent 70%)"></div>
<div class="photo" role="img" aria-label="Rose gold halo diamond ring" style="left:490px;top:1665px;width:100px;height:100px;border-radius:50%;background:radial-gradient(#f4f4f4,#b97c5e 60%,transparent 70%)"></div>
<div class="photo" role="img" aria-label="Yellow diamond ring" style="left:850px;top:1665px;width:100px;height:100px;border-radius:50%;background:radial-gradient(#f1e29a,#9a9a9a 60%,transparent 70%)"></div>
<div class="btn fill" style="left:550px;top:1695px;width:100px;height:28px;font-size:10px;background:#2b2b2b">Add to Cart</div>
<div class="abs" style="left:556px;top:1735px;display:flex;gap:8px">
  <span style="width:22px;height:22px;background:#2b2b2b"></span><span style="width:22px;height:22px;background:#2b2b2b"></span><span style="width:22px;height:22px;background:#2b2b2b"></span>
</div>
<div class="btn fill" style="left:510px;top:1855px;width:180px;height:36px;font-size:11px">View All Collection</div>

<!-- Selecting -->
<div class="abs" style="left:180px;top:2078px;width:430px;height:492px;border:1px solid var(--line)"></div>
<div class="photo" role="img" aria-label="Delighted woman opening a ring box with an engagement ring" style="left:160px;top:2095px;width:450px;height:478px;background:linear-gradient(120deg,#8a6a4c,#d7b694 40%,#e8d6c2 60%,#a07a5a)"></div>
<h2 class="abs serif" style="left:690px;top:2130px;font-size:28px;font-weight:400;line-height:30px">SELECTING YOUR<br>DIAMOND</h2>
<p class="abs copy" style="left:690px;top:2270px;width:350px;font-size:12.5px">We want to take the stress out of your all shopping, that's why we offer so many services that help take the pressure off. We're here to provide gifting ideas, personal touches and assurances that make your shopping experience effortless.</p>
<span class="service-icon" style="left:758px;top:2363px"></span>
<span class="service-icon" style="left:943px;top:2363px"></span>
<span class="service-icon" style="left:758px;top:2450px"></span>
<span class="service-icon" style="left:943px;top:2450px"></span>
<div class="service" style="left:690px;top:2395px">FREE SHIPPING</div>
<div class="service" style="left:875px;top:2395px">MONEY BACK GUARANTEE</div>
<div class="service" style="left:690px;top:2482px">GIFT PACKING</div>
<div class="service" style="left:875px;top:2482px">EXCHANGE OR RETURN</div>

<!-- Videos -->
<h2 class="abs heading center" style="top:2775px">Viwe Diamond Videos</h2>
<svg class="divider" style="top:2838px" aria-hidden="true"><line x1="0" y1="7" x2="88" y2="7" stroke="#ccc"/><rect x="95" y="3" width="8" height="8" transform="rotate(45 99 7)" fill="none" stroke="#ccc"/><line x1="112" y1="7" x2="200" y2="7" stroke="#ccc"/></svg>
<div class="abs" style="left:298px;top:2893px;width:604px;height:378px;border:1px solid var(--line)"></div>
<div class="photo" role="img" aria-label="Video still of a twisted halo diamond engagement ring" style="left:300px;top:2895px;width:600px;height:374px;background:radial-gradient(ellipse at 50% 50%,#e6e6e6,#8d8d8d 40%,#2a2a2a 75%)"></div>
<svg class="abs" style="left:570px;top:3050px" width="60" height="60" aria-hidden="true"><circle cx="30" cy="30" r="24" fill="#fff"/><polygon points="25,19 25,41 42,30" fill="#111"/></svg>
<svg class="abs" style="left:170px;top:3065px" width="860" height="30" aria-hidden="true">
  <path d="M22 2 L8 15 L22 28" stroke="#888" fill="none" stroke-width="2"/>
  <path d="M838 2 L852 15 L838 28" stroke="#888" fill="none" stroke-width="2"/>
</svg>

<!-- Instagram -->
<h2 class="abs heading center" style="top:3458px">Follow As On Instagram</h2>
<div class="photo" role="img" aria-label="Hands with solitaire ring" style="left:0;top:3580px;width:240px;height:172px;background:linear-gradient(135deg,#e8d4c6,#c29e8a)"></div>
<div class="photo" role="img" aria-label="Gold wedding bands" style="left:240px;top:3580px;width:240px;height:172px;background:linear-gradient(135deg,#dcd8cc,#a59a7e)"></div>
<div class="photo" role="img" aria-label="Jewellery lifestyle shot" style="left:480px;top:3580px;width:240px;height:172px;background:#b28b79"></div>
<div class="btn" style="left:555px;top:3630px;width:90px;height:26px;font-size:10px;background:#2b2b2b;border-color:#2b2b2b">Shop Now</div>
<span class="abs" style="left:590px;top:3665px;width:20px;height:20px;background:#2b2b2b"></span>
<div class="photo" role="img" aria-label="Couple in jewellery store" style="left:720px;top:3580px;width:240px;height:172px;background:linear-gradient(135deg,#cfc0b0,#7e6a5a)"></div>
<div class="photo" role="img" aria-label="Jeweller at work" style="left:960px;top:3580px;width:240px;height:172px;background:linear-gradient(135deg,#caa07a,#4e3a2c)"></div>
<div class="photo" role="img" aria-label="Hands holding ring" style="left:0;top:3752px;width:240px;height:172px;background:linear-gradient(135deg,#f0e4dc,#c8a896)"></div>
<div class="photo" role="img" aria-label="Ring on finger" style="left:240px;top:3752px;width:240px;height:172px;background:linear-gradient(135deg,#5c5c5c,#d2b4a2)"></div>
<div class="photo" role="img" aria-label="Platinum bands on dark surface" style="left:480px;top:3752px;width:240px;height:172px;background:linear-gradient(135deg,#3a3a3a,#c8c8c8)"></div>
<div class="photo" role="img" aria-label="Ring being fitted" style="left:720px;top:3752px;width:240px;height:172px;background:linear-gradient(135deg,#b9a898,#6a5648)"></div>
<div class="photo" role="img" aria-label="Rose gold rings stacked" style="left:960px;top:3752px;width:240px;height:172px;background:linear-gradient(135deg,#e6c6ae,#9a6e56)"></div>

<!-- Newsletter -->
<h2 class="abs heading center" style="top:4112px;font-size:27px">Subscribe To The Hollis Fenwick Newsletter</h2>
<div class="abs field">Email Address *</div>
<div class="btn fill" style="left:665px;top:4232px;width:185px;height:36px;font-size:11px">Subscribe Today</div>

<!-- Footer -->
<div class="abs" style="left:0;top:4312px;width:1200px;height:1px;background:#333"></div>
<div class="abs center footer-links" style="top:4340px">Browse Collection &nbsp;|&nbsp; Videos &nbsp;|&nbsp; Online Shop &nbsp;|&nbsp; About Our Diamonds &nbsp;|&nbsp; History Of HF &nbsp;|&nbsp; Contact Us &nbsp;|<br>Email Customer Service &nbsp;|&nbsp; Shipping &amp; Returns &nbsp;|&nbsp; Privacy Policy &nbsp;|&nbsp; Language ▾</div>
<div class="abs copy" style="left:180px;top:4452px;font-size:11px">© 2017 Hollis Fenwick Pty Ltd . All Rights Reserved.</div>
<div class="abs" style="left:585px;top:4454px;display:flex;gap:14px">
  <span style="width:30px;height:14px;background:#444"></span><span style="width:30px;height:14px;background:#444"></span><span style="width:30px;height:14px;background:#444"></span><span style="width:30px;height:14px;background:#444"></span>
</div>
<div class="abs" style="left:935px;top:4449px;display:flex;gap:10px">
  <span style="width:22px;height:22px;border-radius:50%;background:#3d5c9a"></span><span style="width:22px;height:22px;border-radius:50%;background:#e0e0e0"></span><span style="width:22px;height:22px;border-radius:50%;background:#e0e0e0"></span>
</div>
</body>
</html>
```